BrightCampusPicks blogger needs pagely book cover

The title for the book is "Mapping School Options: A Handbook for Reading Campus Pages to Spend Little on a Stronger Degree"

Title must legible for Pagely store. I only need to front, no back or spine. The cover should be optimized to display on Vornex. Image size should be 1880x2500.

This book isn’t about how to apply to college or which classes to take or how to score higher on the QRT. It’s only focus is on how to use college websites to create a better college list. This is part of my general approach for families to use information important to their situation to find affordable colleges. I've attached a file with some covers from the category I like. I'm pretty flexible regarding colors, fonts, etc.

Target Market(s)

Parents of high school students worried about paying for college.

Industry/Entity Type

College

Requirements
Must have
• Title must be legible at small size.

```html
<!DOCTYPE html>
<html lang="en">
<head>
<meta charset="utf-8">
<title>Mapping School Options – Book Cover</title>
<link rel="stylesheet" href="https://fonts.googleapis.com/css2?family=Courier+Prime:wght@400;700&family=Lora:wght@400;500&display=swap">
<style>
  :root {
    --bg-top: #f4f4fb;
    --bg-bottom: #e3ebf8;
    --grid-line: rgba(150, 172, 214, 0.28);
    --paper: #fbfbfd;
    --paper-rule: #c9d3e8;
    --paper-margin: #e6b9c6;
    --tape: rgba(210, 218, 234, 0.78);
    --ink: #2f3036;
    --navy: #1f2d4a;
    --art-light: #f8d3e4;
    --art-deep: #f0b6d2;
  }
  * { margin: 0; padding: 0; box-sizing: border-box; }
  html, body { width: 865px; height: 1200px; overflow: hidden; }
  body { background: #ffffff; }

  .cover {
    position: relative;
    width: 865px;
    height: 1200px;
    overflow: hidden;
    background: linear-gradient(180deg, var(--bg-top) 0%, var(--bg-bottom) 100%);
  }

  .grid {
    position: absolute;
    inset: 0;
    background-image:
      linear-gradient(to right, var(--grid-line) 2px, transparent 2px),
      linear-gradient(to bottom, var(--grid-line) 2px, transparent 2px);
    background-size: 72px 72px;
    background-position: 20px 10px;
    -webkit-mask-image: linear-gradient(180deg, rgba(0,0,0,0.35) 0%, rgba(0,0,0,1) 55%);
    mask-image: linear-gradient(180deg, rgba(0,0,0,0.35) 0%, rgba(0,0,0,1) 55%);
  }

  .torn-note {
    position: absolute;
    left: 66px;
    top: 50px;
    width: 735px;
    height: 550px;
    filter: drop-shadow(0 3px 5px rgba(60, 70, 100, 0.2));
  }

  .tape {
    position: absolute;
    width: 150px;
    height: 50px;
    background: var(--tape);
    box-shadow: 0 1px 3px rgba(80, 90, 120, 0.15);
  }
  .tape--left { left: 34px; top: 50px; transform: rotate(-38deg); }
  .tape--right { right: 40px; top: 40px; transform: rotate(36deg); }

  .title {
    font-family: "Courier Prime", "Courier New", monospace;
    font-weight: 700;
    color: var(--ink);
  }
  .title__line {
    position: absolute;
    left: 0;
    width: 865px;
    text-align: center;
    line-height: 1;
  }
  .title__line--first { top: 175px; font-size: 96px; letter-spacing: 14px; padding-left: 14px; }
  .title__line--second { top: 296px; font-size: 142px; letter-spacing: 4px; padding-left: 4px; }
  .title__line--third { top: 450px; font-size: 96px; letter-spacing: 14px; padding-left: 14px; }

  .savings-art {
    position: absolute;
    left: 300px;
    top: 620px;
    width: 320px;
    height: 240px;
    border-radius: 18px;
    background: linear-gradient(160deg, var(--art-light) 0%, var(--art-deep) 100%);
  }

  .subtitle {
    position: absolute;
    left: 120px;
    top: 878px;
    width: 625px;
    text-align: center;
    font-family: "Lora", Georgia, serif;
    font-weight: 400;
    font-size: 42px;
    line-height: 1.22;
    color: var(--navy);
  }

  .author {
    position: absolute;
    left: 0;
    top: 1100px;
    width: 865px;
    text-align: center;
    font-family: "Courier Prime", "Courier New", monospace;
    font-weight: 700;
    font-size: 50px;
    letter-spacing: 4px;
    line-height: 1;
    color: var(--ink);
  }
</style>
</head>
<body>
  <main class="cover">
    <div class="grid" aria-hidden="true"></div>

    <svg class="torn-note" viewBox="0 0 735 550" aria-hidden="true">
      <path fill="var(--paper)" d="M14 0 L735 6 L731 542 L700 534 L668 546 L630 536 L598 548 L560 537 L520 547 L486 536 L450 544 L410 534 L372 546 L334 535 L296 544 L258 533 L220 545 L184 534 L146 544 L110 532 L74 542 L40 533 L24 505 L14 470 L26 436 L12 400 L24 366 L10 330 L22 296 L8 260 L20 226 L6 190 L18 156 L4 120 L16 86 L2 52 L14 24 Z"/>
      <g stroke="var(--paper-rule)" stroke-width="2">
        <line x1="20" y1="40" x2="732" y2="40"/>
        <line x1="20" y1="232" x2="732" y2="232"/>
        <line x1="20" y1="378" x2="732" y2="378"/>
        <line x1="20" y1="496" x2="732" y2="496"/>
      </g>
      <line x1="88" y1="0" x2="88" y2="538" stroke="var(--paper-margin)" stroke-width="2"/>
    </svg>

    <div class="tape tape--left" aria-hidden="true"></div>
    <div class="tape tape--right" aria-hidden="true"></div>

    <h1 class="title">
      <span class="title__line title__line--first">MAPPING</span>
      <span class="title__line title__line--second">SCHOOL</span>
      <span class="title__line title__line--third">OPTIONS</span>
    </h1>

    <div class="savings-art" role="img" aria-label="Illustration area: pink piggy bank with a gold coin dropping in and a mouse pointer clicking it"></div>

    <p class="subtitle">A Handbook for Reading Campus Pages to Spend Little on a Stronger Degree</p>

    <p class="author">MARLENE HOFFSTADTER</p>
  </main>
</body>
</html>
```